Ciel doux

Hello,
I’m a designer sunglasses reatail Store owner in Montreal, Quebec.

Looking for something modern, fresh with a trendy appeal.

Will send my logo.
Thank you.

Store

```html
<!DOCTYPE html>
<html lang="fr">
<head>
<meta charset="utf-8">
<title>Ciel doux – cartes de visite</title>
<link rel="stylesheet" href="https://fonts.googleapis.com/css2?family=Open+Sans:wght@400;600;700&display=swap">
<style>
  :root {
    --backdrop: #333333;
    --card-white: #ffffff;
    --brand-red: #c41230;
    --ink: #1f1f1f;
    --band-black: #1c1c1c;
    --text: #222222;
  }
  * { margin: 0; padding: 0; box-sizing: border-box; }
  html, body { width: 1200px; height: 900px; overflow: hidden; }
  body {
    background: var(--backdrop);
    font-family: "Open Sans", Arial, sans-serif;
    position: relative;
  }
  .card {
    position: absolute;
    top: 306px;
    width: 439px;
    height: 271px;
    box-shadow: 3px 4px 6px rgba(0,0,0,0.55);
    overflow: hidden;
  }
  .card-front { left: 149px; background: var(--card-white); }
  .card-back { left: 608px; background: var(--brand-red); }

  .name-marker { position: absolute; left: 0; top: 25px; }
  .holder-name {
    position: absolute; left: 33px; top: 28px;
    font-weight: 700; font-size: 16px; color: var(--brand-red);
    letter-spacing: 0.2px;
  }
  .holder-role {
    position: absolute; left: 33px; top: 46px;
    font-size: 12px; color: var(--text);
  }

  .brand-lockup {
    position: absolute; left: 128px; top: 100px;
    display: flex; align-items: center; gap: 12px;
  }
  .brand-dot {
    width: 34px; height: 34px; border-radius: 50%;
    background: var(--brand-red);
  }
  .brand-name {
    font-weight: 600; font-size: 34px; color: var(--ink);
    letter-spacing: 1px; text-transform: uppercase;
  }

  .contact-list {
    position: absolute; left: 26px; top: 193px;
    list-style: none; font-size: 12px; color: var(--text);
  }
  .contact-list li { display: flex; align-items: center; gap: 5px; height: 16px; }
  .contact-list svg { width: 10px; height: 10px; fill: var(--brand-red); }

  .address {
    position: absolute; right: 21px; top: 208px;
    text-align: right; font-size: 12px; line-height: 16px; color: var(--text);
    font-style: normal;
  }
  .base-bands { position: absolute; left: 0; bottom: 0; }

  .back-pattern { position: absolute; inset: 0; background: var(--brand-red); }
  .back-name {
    position: absolute; left: 280px; top: 162px;
    font-weight: 600; font-size: 16px; color: var(--card-white);
    letter-spacing: 1px; text-transform: uppercase;
  }
</style>
</head>
<body>
  <section class="card card-front">
    <svg class="name-marker" width="28" height="38" viewBox="0 0 28 38">
      <polygon points="0,0 12,0 16,38 0,38" fill="var(--band-black)"/>
      <polygon points="14,0 28,0 28,38 18,38" fill="var(--brand-red)"/>
    </svg>
    <h1 class="holder-name">MARC LEBLANC</h1>
    <p class="holder-role">Managing Director</p>

    <div class="brand-lockup">
      <span class="brand-dot"></span>
      <span class="brand-name">Ciel doux</span>
    </div>

    <ul class="contact-list">
      <li><svg viewBox="0 0 10 10"><path d="M2 0.5 L4 2.8 L3 4 Q4.3 6 6 7 L7.2 6 L9.5 8 L8 9.6 Q3.5 9 0.4 2 Z"/></svg>(514)555-0142</li>
      <li><svg viewBox="0 0 10 10"><rect x="0" y="2" width="10" height="6.5"/><polyline points="0,2 5,6 10,2" fill="none" stroke="#fff" stroke-width="1"/></svg>bonjour@cieldoux.ca</li>
      <li><svg viewBox="0 0 10 10"><circle cx="5" cy="5" r="4.6"/><ellipse cx="5" cy="5" rx="2" ry="4.6" fill="none" stroke="#fff" stroke-width="0.8"/></svg>www.cieldoux.ca</li>
    </ul>

    <address class="address">88, Rue Saint-Denis,<br>Montréal, H2X 3K8</address>

    <svg class="base-bands" width="439" height="20" viewBox="0 0 439 20">
      <polygon points="0,6 218,6 206,20 0,20" fill="var(--band-black)"/>
      <polygon points="223,1 439,1 439,20 207,20" fill="var(--brand-red)"/>
    </svg>
  </section>

  <section class="card card-back">
    <div class="back-pattern" role="img" aria-label="Motif répété de la marque en rouge ton sur ton"></div>
    <span class="back-name">Ciel doux</span>
  </section>
</body>
</html>
```